Create modern and sleek business card for luxury real estate company

We're a "boutique" real estate office looking for a design that gets across a highly modern luxury brand. Blacks and whites are probably the best colors unless we try a silver foil for the logo. I've attached a version of our current logo here. I'd like to swap out the current font on there with Gotham Light Regular.

I'm looking to have one side of the card have the logo with the space for our agents info on the other side.

Target Market(s)

Young professionals in a "luxury" headspace

Industry/Entity Type

Real estate

Contact Information for Business Card

A place for agent name, cell number, website. The slogan "Quietly Redefining Home Living".

Font styles to use
Other font styles liked:
• Gotham Regular

Colors

Designer to choose only greyscale colors for use in the design.

Requirements
Must have
• Matte black as the background color. Clean lines and use of contrast. A specific design aspect that will use silver foil.
Nice to have
• Up in the air on integrating a QR code
Should not have
• Any houses or other real estate related design (ex: a clip art house)

```html
<!DOCTYPE html>
<html lang="en">
<head>
<meta charset="utf-8">
<title>Halden Realty — Business Card</title>
<link rel="stylesheet" href="https://fonts.googleapis.com/css2?family=Montserrat:wght@300;500;600;700&display=swap">
<style>
  :root {
    --backdrop: #d9d9d9;
    --card-black: #24272b;
    --silver: #d6d6d6;
    --silver-soft: #c4c4c4;
    --ghost: #33373c;
  }
  * { margin: 0; padding: 0; box-sizing: border-box; }
  html, body {
    width: 1200px;
    height: 1200px;
    overflow: hidden;
    background: var(--backdrop);
    font-family: "Montserrat", "Helvetica Neue", Arial, sans-serif;
  }
  .sheet {
    width: 1200px;
    height: 1200px;
    display: flex;
    align-items: center;
    justify-content: center;
    gap: 40px;
  }
  .card {
    position: relative;
    width: 540px;
    height: 540px;
    background: var(--card-black);
    color: var(--silver);
    overflow: hidden;
    box-shadow: 0 18px 40px rgba(0,0,0,0.25);
  }

  /* Front: brand + agent details */
  .brand {
    position: absolute;
    top: 80px;
    left: 110px;
    display: flex;
    align-items: center;
    gap: 22px;
  }
  .brand-dot {
    width: 108px;
    height: 108px;
    border-radius: 50%;
    border: 3px solid var(--silver);
    flex: none;
  }
  .brand-name {
    font-weight: 300;
    font-size: 40px;
    line-height: 1.1;
    letter-spacing: 2px;
    text-transform: uppercase;
    color: var(--silver);
  }
  .agent-name {
    position: absolute;
    top: 290px;
    left: 0;
    right: 0;
    text-align: center;
    font-weight: 700;
    font-size: 38px;
    letter-spacing: 0.5px;
    color: var(--silver);
  }
  .contact {
    position: absolute;
    top: 392px;
    left: 0;
    right: 0;
    list-style: none;
    text-align: center;
    font-weight: 600;
    font-size: 17px;
    line-height: 1.55;
    color: var(--silver-soft);
  }

  /* Back: tagline over a faint ring */
  .ring {
    position: absolute;
    top: 30px;
    left: 30px;
    width: 480px;
    height: 480px;
    border-radius: 50%;
    border: 6px solid var(--ghost);
  }
  .tagline {
    position: absolute;
    top: 232px;
    left: 0;
    right: 0;
    text-align: center;
    font-weight: 600;
    font-size: 21px;
    color: var(--silver-soft);
  }
</style>
</head>
<body>
  <main class="sheet">
    <section class="card card-front">
      <div class="brand">
        <span class="brand-dot"></span>
        <span class="brand-name">Halden<br>Realty</span>
      </div>
      <h1 class="agent-name">AGENT NAME</h1>
      <ul class="contact">
        <li>48 Alder Row Westbrook</li>
        <li>555 014 2290</li>
        <li>info@haldenhomes.com</li>
        <li>www.haldenhomes.com</li>
      </ul>
    </section>
    <section class="card card-back">
      <span class="ring"></span>
      <p class="tagline">Quietly Redefining Home Living</p>
    </section>
  </main>
</body>
</html>
```